Communication and Marketing agency needs a new presentation card

We are a group of communication and marketing agencies specialized in companies that are in the logistics and industrial sector. The head agency is TELVANO Grupo and the group consists of 4 agencies: TELVANO Media, TELVANO Digital, TELVANO Research and EnlazaPorImagen. We hace 4 offices in Spain (Madrid, Barcelona, Valencia and Murcia). We are looking for a clean and attractive design that transmits our experience, brand presence in the market and knowledge to those who receive the card.It has to maintain the colors of the logo that is attached.
Target Market(s)
logistics and industrial sector
Marketing department
Clean and attractive design

```html
<!DOCTYPE html>
<html lang="en">
<head>
<meta charset="utf-8">
<title>TELVANO Grupo – Business Card</title>
<link rel="stylesheet" href="https://fonts.googleapis.com/css2?family=Open+Sans:wght@400;600&display=swap">
<style>
  :root {
    --stage: #242424;
    --card-dark: #121212;
    --card-dark-2: #1c1c1c;
    --texture: #2e2e2e;
    --band: #030303;
    --red: #ff0000;
    --red-mid: #cc0000;
    --red-deep: #990000;
    --brand-red: #d40000;
    --white: #ffffff;
  }
  html, body {
    margin: 0;
    padding: 0;
    width: 1200px;
    height: 1200px;
    overflow: hidden;
    background: var(--stage);
  }
  .canvas {
    display: block;
    width: 1200px;
    height: 1200px;
  }
  .group-name, .tagline, .brand-name {
    font-family: "Open Sans", Arial, sans-serif;
  }
  .group-name { font-size: 36px; font-weight: 400; fill: var(--brand-red); }
  .tagline { font-size: 21px; font-weight: 400; }
  .tagline .accent { fill: var(--red); }
  .tagline .plain { fill: var(--white); }
  .brand-name { font-weight: 600; fill: var(--brand-red); }
  .icon-disc { fill: var(--brand-red); }
  .icon-glyph { fill: #1a0000; }
  .icon-line { fill: none; stroke: #1a0000; stroke-width: 1.6; }
</style>
</head>
<body>
<svg class="canvas" viewBox="0 0 1257 1257" xmlns="http://www.w3.org/2000/svg">
  <defs>
    <filter id="card-shadow" x="-20%" y="-20%" width="140%" height="140%">
      <feGaussianBlur stdDeviation="18"/>
    </filter>
    <filter id="soft-edge" x="-20%" y="-20%" width="140%" height="140%">
      <feGaussianBlur stdDeviation="6"/>
    </filter>
    <linearGradient id="front-dark" x1="0" y1="0" x2="0" y2="1">
      <stop offset="0" stop-color="#151515"/>
      <stop offset="1" stop-color="#1d1d1d"/>
    </linearGradient>
    <linearGradient id="red-arc" x1="0" y1="0" x2="0" y2="1">
      <stop offset="0" stop-color="#ff0000"/>
      <stop offset="0.35" stop-color="#e00000"/>
      <stop offset="0.7" stop-color="#b00000"/>
      <stop offset="1" stop-color="#ff1a1a"/>
    </linearGradient>
    <clipPath id="front-clip"><rect x="195" y="45" width="900" height="525"/></clipPath>
    <clipPath id="back-clip"><rect x="195" y="657" width="898" height="525"/></clipPath>
  </defs>

  <!-- Card shadows -->
  <rect x="205" y="60" width="900" height="525" fill="#000" opacity="0.55" filter="url(#card-shadow)"/>
  <rect x="205" y="672" width="898" height="525" fill="#000" opacity="0.55" filter="url(#card-shadow)"/>

  <!-- FRONT CARD -->
  <g class="card-front" clip-path="url(#front-clip)">
    <rect x="195" y="45" width="900" height="525" fill="url(#front-dark)" role="img" aria-label="Dark carbon-fibre texture"/>
    <path class="disc-shadow" d="M820,45 Q700,300 830,570" fill="none" stroke="#000" stroke-width="22" opacity="0.8" filter="url(#soft-edge)"/>
    <path class="textured-disc" d="M820,45 Q700,300 830,570 L1095,570 L1095,45 Z" fill="var(--texture)" role="img" aria-label="Perforated metal texture"/>
    <path class="red-crescent" d="M750,120 Q668,300 740,480 L756,480 Q705,300 752,120 Z" fill="url(#red-arc)"/>
    <g class="colour-bars">
      <rect x="765" y="481" width="111" height="53" fill="var(--red)"/>
      <rect x="876" y="481" width="107" height="53" fill="var(--red-mid)"/>
      <rect x="983" y="481" width="112" height="53" fill="var(--red-deep)"/>
    </g>
    <rect class="name-band" x="195" y="207" width="505" height="80" fill="var(--band)"/>
    <text class="group-name" x="458" y="252" text-anchor="middle">TELVANO GRUPO</text>
    <text class="tagline" x="450" y="272" text-anchor="middle"><tspan class="accent">The head</tspan> <tspan class="plain">agency</tspan></text>

    <g class="contact-icons">
      <g class="icon-phone">
        <circle class="icon-disc" cx="252" cy="340" r="19"/>
        <path class="icon-glyph" d="M244,330 l5,-2 l3,6 l-3,2 q2,5 7,8 l2,-3 l6,3 l-2,5 q-10,1 -17,-9 q-3,-5 -1,-10 z"/>
      </g>
      <g class="icon-globe">
        <circle class="icon-disc" cx="252" cy="400" r="19"/>
        <circle class="icon-line" cx="252" cy="400" r="10"/>
        <ellipse class="icon-line" cx="252" cy="400" rx="4.5" ry="10"/>
        <line class="icon-line" x1="242" y1="400" x2="262" y2="400"/>
      </g>
      <g class="icon-mail">
        <circle class="icon-disc" cx="252" cy="452" r="19"/>
        <rect class="icon-glyph" x="242" y="445" width="20" height="14" rx="1"/>
        <path d="M242,446 L252,454 L262,446" fill="none" stroke="#cc0000" stroke-width="1.5"/>
      </g>
      <g class="icon-pin">
        <circle class="icon-disc" cx="252" cy="505" r="19"/>
        <path class="icon-glyph" d="M252,516 q-8,-9 -8,-14 a8,8 0 0 1 16,0 q0,5 -8,14 z"/>
        <circle cx="252" cy="502" r="3" fill="#cc0000"/>
      </g>
    </g>

    <text class="brand-name" x="912" y="285" text-anchor="middle" font-size="40">EnlazaPorImagen</text>
  </g>

  <!-- BACK CARD -->
  <g class="card-back" clip-path="url(#back-clip)">
    <rect x="195" y="657" width="898" height="525" fill="var(--texture)" role="img" aria-label="Perforated metal texture"/>
    <path class="ring-shadow" d="M470,657 Q290,920 470,1182" fill="none" stroke="#000" stroke-width="20" opacity="0.85" filter="url(#soft-edge)"/>
    <path class="ring-shadow" d="M820,657 Q1000,920 820,1182" fill="none" stroke="#000" stroke-width="20" opacity="0.85" filter="url(#soft-edge)"/>
    <path class="red-crescent" d="M392,732 Q290,910 390,1090 L404,1090 Q336,910 404,732 Z" fill="url(#red-arc)"/>
    <path class="red-crescent" d="M892,732 Q994,910 894,1090 L880,1090 Q948,910 880,732 Z" fill="url(#red-arc)"/>
    <text class="brand-name" x="645" y="905" text-anchor="middle" font-size="44">EnlazaPorImagen</text>
  </g>
</svg>
</body>
</html>
```